Multi-Line Insurance PPC Landing Page - Conversion optimized.

We have a PPC landing page used for the general population to get an insurance quote through an agent's site.

We'd like to improve the page for PPC traffic, make it more conversion friendly.

Site should be a single long page.

We will dynamically change the form and headlines on the page depending on what insurance "line" is being called. ie, Lift, Auto, Home, Business.

The enclosed AI file has all of the raw elements we need. We're looking to enhance the design and conversion ability.

Target Market(s)

General public needed insurance services.

Industry/Entity Type

Insurance Broker

Number of Pages Required

1 page

Font styles to use
Sans Serif

Requirements
Must have
• Form, agent picture, name, address.

```html
<!DOCTYPE html>
<html lang="en">
<head>
<meta charset="utf-8">
<title>Insurance Agent</title>
<link href="https://fonts.googleapis.com/css2?family=Cinzel:wght@400;700&family=Open+Sans:wght@400;600;700&display=swap" rel="stylesheet">
<style>
:root{
  --blue:#1690d8;
  --blue-dark:#0f6fb3;
  --navy:#1d4f91;
  --ink:#333;
  --muted:#666;
  --light:#ececec;
  --line:#d6d6d6;
  --white:#fff;
}
*{box-sizing:border-box;margin:0;padding:0}
html,body{width:1200px;height:2232px;overflow:hidden}
body{font-family:"Open Sans",Arial,sans-serif;color:var(--ink);background:var(--white);position:relative}
.serif{font-family:"Cinzel",Georgia,serif}

.site-header{height:72px;display:flex;align-items:center;justify-content:space-between;padding:0 60px}
.brand{font-family:"Cinzel",Georgia,serif;font-size:36px;font-weight:700;color:var(--navy);letter-spacing:1px}
.header-phone{display:flex;align-items:center;gap:10px;color:var(--navy);font-size:22px}

.hero{position:absolute;top:72px;left:0;width:1200px;height:410px;background:var(--blue)}
.hero-art{position:absolute;left:640px;top:20px;width:360px;height:390px;border-radius:180px 180px 0 0;background:linear-gradient(180deg,#4fb0e8,#2a9be0)}
.hero-text{position:absolute;left:130px;top:175px;width:420px;color:var(--white);font-size:25px;line-height:34px;font-weight:600}
.btn{display:inline-block;background:var(--navy);color:var(--white);font-size:14px;font-weight:700;padding:7px 16px;letter-spacing:.5px}
.hero .btn{position:absolute;left:130px;top:288px;background:var(--white);color:var(--navy)}

.quote-card{position:absolute;top:478px;left:130px;width:940px;height:346px;background:var(--white);box-shadow:0 2px 10px rgba(0,0,0,.2);border-top:4px solid var(--blue)}
.agent{position:absolute;left:30px;top:40px;width:200px;text-align:center}
.agent-photo{width:110px;height:110px;margin:0 auto 12px;background:linear-gradient(180deg,#c9d2db,#556371)}
.agent-name{font-family:"Cinzel",Georgia,serif;color:var(--blue);font-size:17px;font-weight:700}
.agent-line{font-size:13px;color:var(--muted);margin-top:6px;display:flex;justify-content:center;align-items:center;gap:6px}
.agent-note{font-size:12px;color:var(--muted);margin-top:10px;line-height:16px}
.quote-title{position:absolute;left:260px;top:16px;width:660px;text-align:center;font-family:"Cinzel",Georgia,serif;font-size:25px;color:var(--blue);font-weight:700}
.quote-form{position:absolute;left:270px;top:60px;width:640px;display:grid;grid-template-columns:1fr 1fr;column-gap:40px;row-gap:8px}
.field label{display:block;font-size:12px;color:var(--muted);margin-bottom:3px}
.field .input{height:28px;border:1px solid var(--line);background:#fafafa;font-size:12px;color:#999;padding:5px 8px}
.field .split{display:flex;gap:6px}
.field .split .input{flex:1}
.submit{position:absolute;left:630px;top:302px;width:120px;text-align:center;padding:8px 0}

.about{position:absolute;top:850px;left:0;width:1200px;height:160px;background:var(--light);text-align:center}
.section-title{font-family:"Cinzel",Georgia,serif;font-size:27px;color:var(--navy);font-weight:700}
.section-title span{color:var(--blue)}
.rule{width:90px;height:2px;background:var(--navy);margin:8px auto 14px}
.about .section-title{margin-top:20px}
.about p{width:1040px;margin:0 auto;font-size:13px;line-height:18px;color:var(--muted)}

.products{position:absolute;top:1030px;left:0;width:1200px;text-align:center}
.product-row{display:flex;justify-content:center;gap:60px;margin-top:26px}
.product{width:200px}
.product svg{height:82px}
.product h3{font-family:"Cinzel",Georgia,serif;color:var(--blue);font-size:20px;margin-top:30px}
.product p{font-size:12px;line-height:16px;color:var(--muted);margin:8px 0 12px}

.testimonials{position:absolute;top:1450px;left:0;width:1200px;height:320px;background:var(--light);text-align:center}
.testimonials .section-title{margin-top:16px}
.t-row{position:relative;height:230px}
.t-photo{position:absolute;border-radius:50%;background:linear-gradient(180deg,#d9c9bd,#8b6e5f);border:4px solid var(--white)}
.t-main{left:540px;top:0;width:120px;height:120px}
.t-side1{left:180px;top:40px;width:90px;height:90px;opacity:.8}
.t-side2{left:925px;top:40px;width:90px;height:90px;opacity:.8}
.t-name{position:absolute;top:132px;left:0;width:1200px;font-family:"Cinzel",Georgia,serif;color:var(--blue);font-size:15px;font-weight:700}
.t-quote{position:absolute;top:156px;left:380px;width:440px;font-size:12px;line-height:16px;color:var(--muted)}
.arrow{position:absolute;top:60px}

.companies{position:absolute;top:1850px;left:0;width:1200px;text-align:center}
.company-row{display:flex;justify-content:center;align-items:center;gap:70px;margin-top:40px}
.company{font-size:30px;font-weight:700;color:#555}

.site-footer{position:absolute;top:2090px;left:0;width:1200px;height:142px;background:var(--navy);color:var(--white);text-align:center;font-size:12px;line-height:16px;padding-top:22px}
.site-footer strong{display:block;margin-bottom:4px}
.site-footer .copy{margin-top:26px;font-size:12px}
</style>
</head>
<body>

<header class="site-header">
  <div class="brand">Insurance Agent</div>
  <div class="header-phone">
    <svg width="22" height="22" viewBox="0 0 24 24"><circle cx="12" cy="12" r="11" fill="none" stroke="#1d4f91" stroke-width="2"/><path d="M8 6l2 0 1 3-1.5 1a7 7 0 0 0 4 4l1-1.5 3 1v2a1.5 1.5 0 0 1-1.5 1.5A10 10 0 0 1 6.5 7.5 1.5 1.5 0 0 1 8 6z" fill="#1d4f91"/></svg>
    123 456 7890
  </div>
</header>

<section class="hero">
  <div class="hero-art" role="img" aria-label="Illustration of a family sheltered under a large umbrella"></div>
  <div class="hero-text">Lorem ipsum dolor sit amet, consectetur adipiscing elit sed diam</div>
  <span class="btn">GET A QUOTE!</span>
</section>

<section class="quote-card">
  <div class="agent">
    <div class="agent-photo" role="img" aria-label="Portrait photo of the insurance agent"></div>
    <div class="agent-name">Lorem Ipsum Dolor</div>
    <div class="agent-line">
      <svg width="13" height="13" viewBox="0 0 24 24"><circle cx="12" cy="12" r="11" fill="#1690d8"/><path d="M8 6h2l1 3-1.5 1a7 7 0 0 0 4 4l1-1.5 3 1v2A10 10 0 0 1 6.5 7.5z" fill="#fff"/></svg>
      123 456 7890
    </div>
    <div class="agent-line">
      <svg width="13" height="13" viewBox="0 0 24 24"><rect x="2" y="5" width="20" height="14" fill="#1690d8"/><path d="M2 5l10 8 10-8" stroke="#fff" stroke-width="2" fill="none"/></svg>
      hello@agentsite.com
    </div>
    <div class="agent-note">Lorem ipsum dolor sit amet, conse adipiscing elit sed diam nonummy nibh euismod tincidunt</div>
  </div>

  <div class="quote-title">Get An Instant Insurance Quote.</div>

  <div class="quote-form">
    <div class="field"><label>Full Name:</label><div class="input"></div></div>
    <div class="field"><label>Home Phone:</label><div class="input"></div></div>
    <div class="field"><label>Zip:</label><div class="input">Select</div></div>
    <div class="field"><label>Address line:</label><div class="input">Select</div></div>
    <div class="field"><label>Date of Birth:</label><div class="split"><div class="input">Month</div><div class="input">Day</div><div class="input">Year</div></div></div>
    <div class="field"><label>Mobile:</label><div class="input"></div></div>
    <div class="field"><label>Current Insurer:</label><div class="input">Select</div></div>
    <div class="field"><label>Email:</label><div class="input"></div></div>
  </div>
  <span class="btn submit">SUBMIT</span>
</section>

<section class="about">
  <h2 class="section-title"><span>About</span> Insurance Agent</h2>
  <div class="rule"></div>
  <p>Lorem ipsum dolor sit amet, consectetuer adipiscing elit, sed diam nonummy nibh euismod tincidunt ut laoreet dolore magna aliquam erat volutpat. Ut wisi enim ad minim veniam, quis nostrud exerci tation ullamcorper suscipit lobortis nisl ut aliquip ex ea commodo consequat. Duis autem vel eum iriure dolor in hendrerit in vulputate velit esse molestie consequat, vel illum dolore eu feugiat nulla facilisis at vero eros et accumsan et iusto odio dignissim qui blandit praesent luptatum zzril delenit augue duis dolore te feugait nulla facilisi.</p>
</section>

<section class="products">
  <h2 class="section-title"><span>Our</span> Insurance Products</h2>
  <div class="rule"></div>
  <div class="product-row">
    <div class="product">
      <svg viewBox="0 0 80 80" width="82"><g fill="#1d4f91"><rect x="10" y="20" width="6" height="50"/><rect x="16" y="58" width="24" height="5"/><rect x="34" y="30" width="28" height="26"/><rect x="44" y="20" width="14" height="12" fill="none" stroke="#1d4f91" stroke-width="4"/><circle cx="42" cy="66" r="7"/><circle cx="62" cy="66" r="7"/></g></svg>
      <h3>Lift</h3>
      <p>Lorem ipsum dolor sit amet, consectetuer adipiscing elit, sed diam nonummy nibh euismod tincidunt</p>
      <span class="btn">GET A QUOTE!</span>
    </div>
    <div class="product">
      <svg viewBox="0 0 80 80" width="82"><g fill="#1d4f91"><path d="M14 40l8-18h36l8 18h4v20H10V40z"/><rect x="26" y="27" width="28" height="11" fill="#fff"/><rect x="12" y="60" width="12" height="10"/><rect x="56" y="60" width="12" height="10"/><circle cx="22" cy="48" r="4" fill="#fff"/><circle cx="58" cy="48" r="4" fill="#fff"/></g></svg>
      <h3>Auto</h3>
      <p>Lorem ipsum dolor sit amet, consectetuer adipiscing elit, sed diam nonummy nibh euismod tincidunt</p>
      <span class="btn">GET A QUOTE!</span>
    </div>
    <div class="product">
      <svg viewBox="0 0 80 80" width="82"><g fill="#1d4f91"><path d="M40 8L6 40h10v32h48V40h10z"/><rect x="34" y="50" width="12" height="22" fill="#fff"/></g></svg>
      <h3>Home</h3>
      <p>Lorem ipsum dolor sit amet, consectetuer adipiscing elit, sed diam nonummy nibh euismod tincidunt</p>
      <span class="btn">GET A QUOTE!</span>
    </div>
    <div class="product">
      <svg viewBox="0 0 80 80" width="82"><g fill="#1d4f91"><rect x="8" y="24" width="64" height="46" rx="4"/><rect x="28" y="12" width="24" height="14" fill="none" stroke="#1d4f91" stroke-width="5"/><rect x="8" y="42" width="64" height="3" fill="#fff"/><rect x="35" y="38" width="10" height="10" fill="#fff"/></g></svg>
      <h3>Business</h3>
      <p>Lorem ipsum dolor sit amet, consectetuer adipiscing elit, sed diam nonummy nibh euismod tincidunt</p>
      <span class="btn">GET A QUOTE!</span>
    </div>
  </div>
</section>

<section class="testimonials">
  <h2 class="section-title"><span>Client</span> Testimonials</h2>
  <div class="rule"></div>
  <div class="t-row">
    <svg class="arrow" style="left:100px" width="20" height="40" viewBox="0 0 20 40"><path d="M18 2L2 20l16 18" stroke="#999" stroke-width="2" fill="none"/></svg>
    <div class="t-photo t-side1" role="img" aria-label="Photo of a client"></div>
    <div class="t-photo t-main" role="img" aria-label="Photo of the featured client"></div>
    <div class="t-photo t-side2" role="img" aria-label="Photo of a client"></div>
    <svg class="arrow" style="left:1080px" width="20" height="40" viewBox="0 0 20 40"><path d="M2 2l16 18L2 38" stroke="#999" stroke-width="2" fill="none"/></svg>
    <div class="t-name">Lorem Ipsum Dolor Sit</div>
    <div class="t-quote">Lorem ipsum dolor sit amet, consectetuer adipiscing elit, sed diam nonummy nibh euismod tincidunt ut laoreet dolore magna aliquam erat volutpat.</div>
  </div>
</section>

<section class="companies">
  <h2 class="section-title"><span>Insurance</span> Company</h2>
  <div class="rule"></div>
  <div class="company-row">
    <span class="company">Harbor Mutual</span>
    <span class="company">Keystone</span>
    <span class="company">Summit Shield</span>
    <span class="company">Prairie Insurance</span>
  </div>
</section>

<footer class="site-footer">
  <strong>Disclaimer :</strong>
  Lorem ipsum dolor sit amet, consectetuer adipiscing elit, sed diam nonummy nibh euismod tincidunt ut laoreet dolore magna aliquam erat volutpat.<br>
  Ut wisi enim ad minim veniam, quis nostrud exerci tation ullamcorper suscipit lobortis nisl ut aliquip ex ea commodo consequat.
  <div class="copy">Copyright © 2015 Insurance Agent &nbsp;|&nbsp; All rights reserved.</div>
</footer>

</body>
</html>
```